Postcard Design

I am an attorney in Pittsburgh. Here and across country, companies are sending data with names, address and new criminal charges for people. This has resulted in some people getting 12 or more of these letters. I want to do a postcard because one does not need to open a postcard. I also want to be delicate since there is no sealed envelope. I want to throw in other matters other than criminal so it does not look like the person is necessarily charged with a crime.
At top would be "Law Office of Dorian F. Haslbeck"
Then:
Need an Attorney?
Attorney Dorian F. Haslbeck has 25 Years of Experience
Free Consultation - Affordable Fees - Credit Cards Accepted
-All Criminal Matters
-Most Civil Matters
-DUI / Traffic Citations / License Restoration
412-555-0187
www.lakesidedefenselawyer.example
www.dfhcounsel.example

My CTQ ranking is A+ but I am not sure they give a logo with the rating. I have all my logos at www.lakesidedefenselawyer.example The purpose of the two websites is these are postcards. I want no one to think oh this person is charged with a crime.

Industry/Entity Type

Attorney

```html
<!DOCTYPE html>
<html lang="en">
<head>
<meta charset="utf-8">
<title>Postcard – Law Office of Dorian F. Haslbeck</title>
<link href="https://fonts.googleapis.com/css2?family=Arimo:wght@400;700&family=Cinzel:wght@400;600&display=swap" rel="stylesheet">
<style>
:root{
  --stage:#939598;
  --navy:#1f2f52;
  --blue-top:#3a64a8;
  --blue-bot:#1d3c74;
  --orange:#f0873a;
  --orange-deep:#e8742a;
  --dark:#1b1b1b;
  --dark2:#2e2e2e;
  --text:#333333;
  --white:#ffffff;
  --placeholder:#e6e7e8;
  --label-text:#9a9a9a;
  --addr-blue:#2d4f8e;
}
*{box-sizing:border-box;margin:0;padding:0}
html,body{width:951px;height:1200px;overflow:hidden;background:var(--stage);font-family:"Arimo",Arial,sans-serif;color:var(--text)}
.canvas{position:relative;width:951px;height:1200px}
.abs{position:absolute}

/* front */
.front{left:46px;top:38px;width:854px;height:551px;background:linear-gradient(115deg,#e9eaec 0%,#f7f7f8 40%,#eceef0 60%,#fafafa 100%);overflow:hidden;box-shadow:0 0 0 1px #cfd0d2}
.masthead{left:0;top:0;width:854px;height:60px;background:linear-gradient(var(--blue-top),var(--blue-bot));border-bottom:5px solid var(--orange);display:flex;align-items:center;justify-content:center}
.masthead h1{font-family:"Cinzel",serif;font-weight:600;color:var(--white);font-size:36px;letter-spacing:1px;white-space:nowrap}
.photo{background:linear-gradient(160deg,#c9cfc2,#7c8a63 55%,#a89a84)}
.photo-family{left:333px;top:65px;width:285px;height:276px}
.photo-officer{left:620px;top:65px;width:234px;height:276px;background:linear-gradient(160deg,#8d949c,#2a3446 55%,#1a1f2a)}
.tagline{left:333px;top:305px;width:521px;height:36px;background:rgba(20,20,20,.82);border-bottom:4px solid var(--orange);color:var(--white);font-size:25px;padding-left:37px;line-height:34px;white-space:nowrap}
.headline{left:40px;top:97px;color:var(--navy);font-weight:700;font-size:52px;line-height:48px}
.experience{left:0;top:212px;width:380px;height:70px;background:var(--orange);border-radius:0 6px 6px 0;color:var(--white);padding:10px 0 0 40px;white-space:nowrap}
.experience .l1{font-size:26px;line-height:28px}
.experience .l2{font-size:25px;font-weight:700;line-height:28px}
.badges{left:33px;top:293px;display:flex;align-items:center;gap:6px}
.cred{display:flex;align-items:center;gap:6px;height:32px;padding:0 8px;background:#1c7f98;color:var(--white);font-size:14px;font-weight:700}
.cred .sq{width:16px;height:16px;background:var(--white)}
.features{left:0;top:370px;width:854px}
.feature{position:absolute;transform:translateX(-50%);text-align:center;font-size:14px;line-height:17px;color:#444;white-space:nowrap}
.feature svg{display:block;margin:0 auto 4px}
.divider{left:0;top:456px;width:854px;height:1px;background:#d0d2d4}
.info-bar{left:0;top:462px;width:854px;height:77px;background:linear-gradient(90deg,var(--dark),var(--dark2) 50%,var(--dark));border-bottom:6px solid var(--orange-deep);color:#e5e5e5}
.address{left:54px;top:10px;font-size:15px;line-height:18.5px;white-space:nowrap}
.schedule{position:absolute;text-align:center;white-space:nowrap}
.schedule .cta{font-size:14px;letter-spacing:.2px;line-height:17px}
.schedule .phone{font-size:31px;color:var(--orange);line-height:33px}
.webs{position:absolute;text-align:center;font-size:14.5px;line-height:18.5px;white-space:nowrap}

/* back */
.back{left:44px;top:620px;width:854px;height:550px;background:var(--white);overflow:hidden;box-shadow:0 0 0 1px #cfd0d2}
.back-panel{left:0;top:0;width:535px;height:550px;background:linear-gradient(115deg,#eeeff1,#fbfbfb 50%,#eef0f1)}
.photo-gavel{left:0;top:0;width:535px;height:209px;background:linear-gradient(170deg,#d9d4cc,#9c8670 55%,#5a3c2a)}
.title-band{left:0;top:167px;width:535px;height:42px;background:rgba(25,20,15,.85);color:var(--white);font-family:"Cinzel",serif;font-size:18px;line-height:42px;padding-left:158px;white-space:nowrap}
.portrait{left:38px;top:135px;width:87px;height:87px;border:2px solid var(--orange);background:linear-gradient(160deg,#8da2b6,#c7b7a8 60%,#6f7b86)}
.quote{top:236px;width:233px;font-size:12px;line-height:15.1px;color:#2b2b2b}
.quote .src{color:var(--orange)}
.back-bar{left:0;top:460px;width:535px;height:82px;background:linear-gradient(90deg,var(--dark),var(--dark2) 50%,var(--dark));border-bottom:6px solid var(--orange-deep);color:#e5e5e5}
.return{left:562px;top:38px}
.return .name{font-family:"Cinzel",serif;font-weight:600;color:var(--addr-blue);font-size:14px;line-height:16px}
.return .lines{margin-top:6px;font-size:10.5px;line-height:12.5px;color:#333}
.stamp{left:757px;top:40px;width:78px;height:78px;background:var(--placeholder)}
.label{left:562px;top:202px;width:266px;height:100px;background:var(--placeholder);color:var(--label-text);font-size:14px;line-height:18px;display:flex;flex-direction:column;align-items:center;justify-content:center}
</style>
</head>
<body>
<div class="canvas">

  <section class="abs front">
    <header class="abs masthead"><h1>Law Office of Dorian F. Haslbeck</h1></header>
    <div class="abs photo photo-family" role="img" aria-label="Smiling family of four in front of their home"></div>
    <div class="abs photo photo-officer" role="img" aria-label="Police officer writing a citation in a patrol car"></div>
    <div class="abs tagline">Experience You Can Afford...</div>

    <h2 class="abs headline">Need an<br>Attorney?</h2>
    <div class="abs experience">
      <div class="l1">Attorney Dorian F. Haslbeck</div>
      <div class="l2">has 25 Years of Experience</div>
    </div>

    <div class="abs badges">
      <div class="cred"><span class="sq"></span>CTQ</div>
      <svg width="30" height="30" aria-hidden="true"><circle cx="15" cy="15" r="15" fill="#1c7f98"/></svg>
      <svg width="58" height="58" style="margin-left:8px" aria-hidden="true"><circle cx="29" cy="29" r="29" fill="#3b2a4a"/></svg>
      <svg width="56" height="56" style="margin-left:22px" aria-hidden="true"><circle cx="28" cy="28" r="28" fill="#2c4a78"/></svg>
    </div>

    <div class="abs features">
      <div class="feature" style="left:79px">
        <svg width="34" height="30" viewBox="0 0 34 30" fill="var(--orange)"><circle cx="7" cy="6" r="3.5"/><circle cx="17" cy="4" r="3.5"/><circle cx="27" cy="6" r="3.5"/><rect x="3" y="11" width="8" height="12" rx="2"/><rect x="13" y="9" width="8" height="9" rx="2"/><rect x="23" y="11" width="8" height="12" rx="2"/><rect x="9" y="18" width="16" height="3"/><rect x="15" y="21" width="4" height="8"/></svg>
        Free<br>Consultation</div>
      <div class="feature" style="left:193px">
        <svg width="34" height="30" viewBox="0 0 34 30" fill="none" stroke="var(--orange)" stroke-width="2.5"><circle cx="12" cy="15" r="10"/><path d="M22 8h10M22 15h10M22 22h10"/><text x="12" y="20" font-size="13" text-anchor="middle" fill="var(--orange)" stroke="none" font-family="Arimo">$</text></svg>
        Affordable<br>Fees</div>
      <div class="feature" style="left:321px">
        <svg width="36" height="30" viewBox="0 0 36 30" fill="none" stroke="var(--orange)" stroke-width="2.5"><rect x="8" y="3" width="26" height="17" rx="2"/><rect x="2" y="10" width="26" height="17" rx="2" fill="#f6f6f6"/><path d="M2 15h26"/></svg>
        Credit Cards<br>Accepted</div>
      <div class="feature" style="left:453px">
        <svg width="36" height="30" viewBox="0 0 36 30" fill="none" stroke="var(--orange)" stroke-width="3"><circle cx="10" cy="19" r="8"/><circle cx="26" cy="13" r="8"/><path d="M16 16l4-2"/></svg>
        All Criminal<br>Matters</div>
      <div class="feature" style="left:578px">
        <svg width="36" height="30" viewBox="0 0 36 30" fill="var(--orange)"><circle cx="7" cy="5" r="3"/><circle cx="18" cy="3" r="3"/><circle cx="29" cy="5" r="3"/><rect x="4" y="10" width="6" height="19" rx="1.5"/><rect x="15" y="8" width="6" height="21" rx="1.5"/><rect x="26" y="10" width="6" height="19" rx="1.5"/></svg>
        Most Civil<br>Matters</div>
      <div class="feature" style="left:722px">
        <svg width="36" height="30" viewBox="0 0 36 30" fill="var(--orange)"><path d="M8 6h20l5 10v11h-6v-4H9v4H3V16z"/><rect x="10" y="9" width="16" height="6" fill="#f6f6f6"/><circle cx="9" cy="19" r="2.5" fill="#f6f6f6"/><circle cx="27" cy="19" r="2.5" fill="#f6f6f6"/></svg>
        DUI / Traffic Citations<br>License Restoration</div>
    </div>

    <div class="abs divider"></div>

    <footer class="abs info-bar">
      <div class="abs address">Dorian F. Haslbeck, Esquire<br>740 Harbor Street Suite 1800<br>Pittsburgh, PA 15222</div>
      <div class="schedule" style="left:310px;width:240px;top:18px">
        <div class="cta">SCHEDULE AN APPINTMENT</div>
        <div class="phone">412-555-0187</div>
      </div>
      <div class="webs" style="left:570px;width:280px;top:22px">www.lakesidedefenselawyer.example<br>www.dfhcounsel.example</div>
    </footer>
  </section>

  <section class="abs back">
    <div class="abs back-panel"></div>
    <div class="abs photo-gavel" role="img" aria-label="Wooden gavel and scales of justice on a desk with law books"></div>
    <div class="abs title-band">Law Office of Dorian F. Haslbeck</div>
    <div class="abs portrait" role="img" aria-label="Portrait of the attorney"></div>

    <p class="abs quote" style="left:38px">&ldquo; Dorian is a true savior.. Only commits to what he can deliver, and delivers it too. No hidden agendas. Had a case from two years back which my previous attorney had me plead guilty to, stating it was just like a speeding ticket. It came back to bite me now and I could have been deported. Lucky I hired Dorian and he explained his course of action clearly.. and worked out all that in my favor. Another plus was that his fees was far less than what other attorneys charged. Always reachable on phone.&rdquo; <span class="src">Client - Counselrate - 2015</span></p>
    <p class="abs quote" style="left:289px">&ldquo; As a former Assistant District Attorney, I had occasion to prosecute Mr. Haslbeck's clients at preliminary hearings and trials. Dorian truly possesses all the qualities needed for effective advocacy: intellect, a strong understanding of the law, a thorough approach to case preparation, and the interpersonal skills needed to relate to both juries and judges alike. Most importantly, he understands what it takes to "reach across the aisle" and negotiate favorable results for his clients.&rdquo; <span class="src">Fellow Attorney - Searchly - 2015</span></p>

    <footer class="abs back-bar">
      <div class="schedule" style="left:36px;top:18px;text-align:left">
        <div class="cta">SCHEDULE AN APPINTMENT</div>
        <div class="phone">412-555-0187</div>
      </div>
      <div class="webs" style="left:250px;width:280px;top:19px">www.lakesidedefenselawyer.example<br>www.dfhcounsel.example</div>
    </footer>

    <div class="abs return">
      <div class="name">Law Office of<br>Dorian F. Haslbeck</div>
      <div class="lines">Dorian F. Haslbeck, Esquire<br>740 Harbor Street Suite 1800<br>Pittsburgh, PA 15222</div>
    </div>
    <div class="abs stamp"></div>
    <div class="abs label"><span>label</span><span>1 by 2 5/8</span></div>
  </section>

</div>
</body>
</html>
```